Brindlow Legal Business Card

I require a corporate business card for a new legal services business.

I do not have a logo, nor do I want one.

I require a clean, neat a professional card for a law firm.

Details:

Business Name: Brindlow Legal
Name: Delia ter Hulst
Title: Corporate Services Manager
Location: Office 14 (Top Floor), Kelvara Business Centre, Dunmore Ash Street, Alotau CBD, Milne Bay Province.
Postal Address: PO Box 537, Alotau, 211, Milne Bay Province, Papua New Guinea.
Contact: T: +675 6428153, F: +675 6427602, M: +675 79154368, E: dterhulst@brindlowqx.com.pg.

I look forward to your design submissions.

Legal

```html
<!DOCTYPE html>
<html lang="en">
<head>
<meta charset="utf-8">
<title>Brindlow Legal Business Card</title>
<link rel="stylesheet" href="https://fonts.googleapis.com/css2?family=Cinzel:wght@400;500&family=Open+Sans:wght@400;600&display=swap">
<style>
  :root {
    --stage: #2b2825;
    --card-black: #141414;
    --mark-ink: #262626;
    --card-white: #ffffff;
    --ink: #1a1a1a;
    --rule: #222222;
  }
  * { box-sizing: border-box; margin: 0; padding: 0; }
  html, body {
    width: 1200px;
    height: 716px;
    overflow: hidden;
    background: var(--stage);
  }
  .canvas {
    position: relative;
    width: 1200px;
    height: 716px;
  }
  .card {
    position: absolute;
    top: 215px;
    width: 500px;
    height: 286px;
    border-radius: 2px;
    box-shadow: 0 10px 30px rgba(0,0,0,0.45);
  }
  .card-front {
    left: 70px;
    background: var(--card-black);
    display: flex;
    flex-direction: column;
    align-items: center;
    justify-content: center;
    gap: 16px;
  }
  .brand-square {
    width: 34px;
    height: 34px;
    background: var(--mark-ink);
  }
  .brand-name {
    font-family: "Cinzel", serif;
    font-weight: 500;
    font-size: 30px;
    letter-spacing: 2px;
    color: var(--mark-ink);
  }
  .card-back {
    left: 630px;
    background: var(--card-white);
    color: var(--ink);
  }
  .contact-block {
    position: absolute;
    top: 40px;
    right: 40px;
    text-align: right;
  }
  .person-name {
    font-family: "Cinzel", serif;
    font-size: 22px;
    letter-spacing: 1px;
  }
  .person-title {
    font-family: "Open Sans", sans-serif;
    font-size: 11px;
    margin-top: 2px;
  }
  .phones, .email {
    font-family: "Open Sans", sans-serif;
    font-size: 11.5px;
    line-height: 1.5;
  }
  .phones { margin-top: 10px; }
  .phones b { font-weight: 600; }
  .divider {
    position: absolute;
    left: 0;
    right: 0;
    top: 152px;
    border-top: 1px solid var(--rule);
  }
  .street-address {
    position: absolute;
    left: 22px;
    top: 166px;
    font-family: "Open Sans", sans-serif;
    font-size: 11px;
    line-height: 1.45;
    font-style: normal;
  }
  .postal-address {
    position: absolute;
    right: 26px;
    bottom: 22px;
    text-align: right;
    font-family: "Open Sans", sans-serif;
    font-weight: 600;
    font-size: 12px;
    line-height: 1.45;
    font-style: normal;
  }
</style>
</head>
<body>
<main class="canvas">
  <section class="card card-front" aria-label="Card front">
    <div class="brand-square"></div>
    <div class="brand-name">Brindlow Legal</div>
  </section>

  <section class="card card-back" aria-label="Card back">
    <div class="contact-block">
      <h1 class="person-name">Delia ter Hulst</h1>
      <p class="person-title">Corporate Services Manager</p>
      <p class="phones">[T] +675 6428153 | [F] +675 6427602 | <b>[M] +675 79154368</b></p>
      <p class="email">dterhulst@brindlowqx.com.pg.</p>
    </div>
    <div class="divider"></div>
    <address class="street-address">
      Office 14 (Top Floor)<br>
      Kelvara Business Centre<br>
      Dunmore Ash Street, Alotau CBD<br>
      Milne Bay Province
    </address>
    <address class="postal-address">
      PO Box 537, Alotau<br>
      211 Milne Bay Province<br>
      Papua New Guinea
    </address>
  </section>
</main>
</body>
</html>
```